Industrial Company-Pop-Up Banner Design for Demolition and Infrastructure Company

Hi-
We need to create 2 pop-up banners for our company. They will both have the same logo, but different photos. We would like to have the colors white, red, and black and feature a modern design. I have attached some inspiration photos.

Target Market(s)

Trade Show/Job Fair Audience

Industry/Entity Type

construction, industrial

Font styles to use
Sans Serif

Colors
EB3D1F
EC4F4E
F09395
F8D3D4
FCEDEE

Requirements
Must have
• 2 versions, each with different photos but same design. Logo, Red, Black, and White Color Scheme, Modern Design
Nice to have
• Modern Design similar to the inspiration photos

```html
<!DOCTYPE html>
<html lang="en">
<head>
<meta charset="utf-8">
<title>R.K. Halden Companies – Pop-Up Banner</title>
<link rel="stylesheet" href="https://fonts.googleapis.com/css2?family=Fjalla+One&family=Kaushan+Script&family=Montserrat:wght@700&display=swap">
<style>
  :root {
    --backdrop: #b8152f;
    --banner-black: #1b1b1c;
    --brand-red: #e32226;
    --white: #ffffff;
    --photo-light: #e4e2df;
    --photo-mid: #a9a7a4;
    --photo-dark: #5e5c5a;
  }
  html, body {
    margin: 0;
    width: 1200px;
    height: 1200px;
    overflow: hidden;
    background: var(--backdrop);
  }
  .canvas {
    position: relative;
    width: 1200px;
    height: 1200px;
  }
  .banner {
    position: absolute;
    left: 302px;
    top: 69px;
    width: 596px;
    height: 1062px;
    display: block;
  }
  .fill-black { fill: var(--banner-black); }
  .fill-red { fill: var(--brand-red); }
  .logo-mark { fill: var(--brand-red); }
  .logo-name {
    font-family: "Montserrat", sans-serif;
    font-weight: 700;
    font-size: 28px;
    fill: var(--white);
  }
  .tagline-lead {
    font-family: "Fjalla One", sans-serif;
    font-size: 36px;
    fill: var(--white);
  }
  .tagline-script {
    font-family: "Kaushan Script", cursive;
    font-size: 112px;
    fill: var(--brand-red);
  }
  .tagline-since {
    font-family: "Montserrat", sans-serif;
    font-weight: 700;
    font-size: 24px;
    letter-spacing: 2px;
    fill: var(--white);
  }
</style>
</head>
<body>
<div class="canvas">
  <svg class="banner" viewBox="0 0 744 1328" xmlns="http://www.w3.org/2000/svg">
    <defs>
      <linearGradient id="photo-tones" x1="0" y1="0" x2="0" y2="1">
        <stop offset="0" stop-color="var(--photo-light)"/>
        <stop offset="0.6" stop-color="var(--photo-mid)"/>
        <stop offset="1" stop-color="var(--photo-dark)"/>
      </linearGradient>
    </defs>

    <rect class="banner-photo" x="0" y="0" width="744" height="1328" fill="url(#photo-tones)"
          role="img" aria-label="Black and white photograph of three striped industrial smokestacks above a plant under a cloudy sky"/>

    <polygon class="corner-panel fill-black" points="237,0 744,0 744,507"/>

    <polygon class="lower-panel fill-black" points="0,419 744,1163 744,1328 0,1328"/>
    <polygon class="diagonal-stripe fill-red" points="0,459 744,1203 744,1289 0,545"/>
    <polygon class="accent-stripe fill-red" points="414,1079 470,1049 744,1323 744,1328 663,1328"/>
    <polygon class="accent-block fill-red" points="477,1274 510,1245 593,1328 531,1328"/>

    <g class="brand-logo">
      <rect class="logo-mark" x="470" y="92" width="22" height="22"/>
      <text class="logo-name" x="504" y="112">R.K. HALDEN</text>
      <text class="logo-name" x="504" y="146">COMPANIES</text>
    </g>

    <g class="tagline">
      <text class="tagline-lead" x="90" y="1126">SHAPING AMERICA’S</text>
      <text class="tagline-script" x="52" y="1220">skyline</text>
      <text class="tagline-since" x="218" y="1250">since 1959</text>
    </g>
  </svg>
</div>
</body>
</html>
```